Join Hour 4 Fun business card

Join Hour 4 Fun is a national UK campaign that promotes the value of play for children. The website has recently undergone a redesign and will soon be going live, this business card design will need to reflect the new website's design and colour scheme, etc.
Key wording/info for inclusion (front)
- Strapline titles
A small Romp each morning (in caps)
giving you great free play ideas, everyday!
- Logo
Key wording for inclusion (rear)
- Download our free play app - Join Hour 4 Fun
- Visit our website - www.joinhour4fun.co.uk
- To share hints and tips with other parents
www.facebook.com/joinhourforfun
- Want to get involved in the campaign? No matter who you are we would love to hear from you! Email - getinvolved@joinhourforfun.co.uk
Social media icons
Facebook facebook.com/joinhour4fun
Twitter @joinhour4fun
Youtube youtube.com/joinhourforfun
The target audience is parents of young children up to the age of 12.
Please note that all attached graphics are the property of the Northern Craft & Pastime Guild and must only be used for the purpose of this project.
Updates
Please note the design we are seeking will be in a business card 'shape' but will not be for a specific 'person' or name as such. We are looking for a colourful and modern design which is not 'corporate. Thank you.
Target Market(s)
Industry/Entity Type
Business
Look and feel

```html
<!DOCTYPE html>
<html lang="en">
<head>
<meta charset="utf-8">
<title>Join Hour 4 Fun – Business Card</title>
<link rel="stylesheet" href="https://fonts.googleapis.com/css2?family=Alfa+Slab+One&family=Open+Sans:wght@400;600&display=swap">
<style>
  :root {
    --bg: #ecebe8;
    --sky-top: #6cc5ec;
    --sky-low: #c4e9f7;
    --band: #ffffff;
    --grass-dark: #2f9c45;
    --grass-light: #8cc63f;
    --ink: #2b2b2b;
    --ink-grass: #163a1c;
    --pink: #e8559a;
    --lime: #a6c939;
    --blue: #2fb4e0;
    --yellow: #f7c234;
    --purple: #8a5bb8;
    --teal: #17a9d8;
    --shadow: 0 14px 30px rgba(0,0,0,.22);
  }
  * { box-sizing: border-box; margin: 0; padding: 0; }
  html, body { width: 1200px; height: 800px; overflow: hidden; }
  body { background: var(--bg); font-family: "Open Sans", sans-serif; position: relative; }

  /* Rear card */
  .card-back {
    position: absolute; left: 70px; top: 122px;
    width: 360px; height: 556px; border-radius: 18px; overflow: hidden;
    display: flex; box-shadow: var(--shadow);
  }
  .stripe { flex: 1; position: relative; padding: 22px 0 0; }
  .stripe--pink { background: var(--pink); }
  .stripe--lime { background: var(--lime); }
  .stripe--blue { background: var(--blue); }
  .stripe--yellow { background: var(--yellow); }
  .stripe__mark {
    display: block; width: 26px; height: 26px; border-radius: 50%;
    background: rgba(255,255,255,.75); margin: 0 auto 16px;
  }
  .stripe__text {
    writing-mode: vertical-rl; position: relative; z-index: 2;
    margin: 0 auto; height: 480px;
    font-size: 15px; line-height: 22px; color: var(--ink);
  }
  .back-photo {
    position: absolute; inset: 0; z-index: 1; pointer-events: none;
    background: radial-gradient(ellipse at 45% 40%, rgba(255,255,255,.35), rgba(255,255,255,0) 70%);
  }

  /* Front card */
  .card-front {
    position: absolute; left: 490px; top: 193px;
    width: 640px; height: 414px; border-radius: 18px; overflow: hidden;
    box-shadow: var(--shadow);
  }
  .front-sky {
    position: absolute; inset: 0;
    background: linear-gradient(180deg, var(--sky-top), var(--sky-low) 60%, var(--sky-top));
  }
  .front-scene { position: absolute; inset: 0; }
  .brand {
    position: absolute; top: 92px; left: 0; right: 0; text-align: center;
    font-family: "Open Sans", sans-serif; font-weight: 600; font-size: 40px;
    color: var(--purple);
  }
  .strapline {
    position: absolute; top: 168px; left: 0; right: 0; text-align: center;
    font-family: "Alfa Slab One", serif; font-weight: 400; font-size: 30px; letter-spacing: 1px;
    text-transform: uppercase;
  }
  .strapline .w1 { color: var(--yellow); }
  .strapline .w2 { color: var(--teal); }
  .strapline .w3 { color: var(--lime); }
  .strapline .w4 { color: var(--pink); }
  .tagline {
    position: absolute; top: 218px; left: 0; right: 0; text-align: center;
    font-size: 19px; color: var(--ink);
  }
  .social {
    position: absolute; left: 32px; right: 32px; bottom: 26px;
    display: flex; justify-content: space-between; list-style: none;
  }
  .social__item { display: flex; align-items: center; gap: 8px; font-size: 17px; color: var(--ink-grass); }
  .social__icon { width: 22px; height: 22px; background: rgba(255,255,255,.7); border-radius: 3px; }
</style>
</head>
<body>

<section class="card-back" aria-label="Business card, reverse">
  <div class="stripe stripe--pink">
    <span class="stripe__mark"></span>
    <p class="stripe__text">Want to get involved in the campaign?<br>No matter who you are we would love to hear from you!<br>Email - getinvolved@joinhourforfun.co.uk</p>
  </div>
  <div class="stripe stripe--lime">
    <span class="stripe__mark"></span>
    <p class="stripe__text">To share hints and tips with other parents:<br>www.parentpages.co.uk/joinhourforfun</p>
  </div>
  <div class="stripe stripe--blue">
    <span class="stripe__mark"></span>
    <p class="stripe__text">Visit our website - www.joinhour4fun.co.uk</p>
  </div>
  <div class="stripe stripe--yellow">
    <span class="stripe__mark"></span>
    <p class="stripe__text">Download our free play app - Join Hour 4 Fun</p>
  </div>
  <div class="back-photo" role="img" aria-label="Faint photograph of children playing"></div>
</section>

<section class="card-front" aria-label="Business card, front">
  <div class="front-sky" role="img" aria-label="Illustrated blue sky with clouds"></div>
  <svg class="front-scene" width="640" height="414" viewBox="0 0 640 414" role="img" aria-label="Illustrated grassy hills">
    <defs>
      <linearGradient id="grass" x1="0" y1="0" x2="0" y2="1">
        <stop offset="0" stop-color="#8cc63f"/>
        <stop offset="1" stop-color="#2f9c45"/>
      </linearGradient>
    </defs>
    <path d="M0 74 C110 52 200 96 320 70 C440 44 540 86 640 62 L640 300 C540 322 440 280 320 306 C200 332 110 290 0 312 Z" fill="#ffffff"/>
    <path d="M0 300 C110 278 200 322 320 296 C440 270 540 312 640 290 L640 414 L0 414 Z" fill="url(#grass)"/>
  </svg>
  <div class="brand">Join Hour 4 Fun</div>
  <h1 class="strapline"><span class="w1">A small</span> <span class="w2">Romp</span> <span class="w3">each</span> <span class="w4">morning</span></h1>
  <p class="tagline">Giving You Great Free Play Ideas, Everyday!</p>
  <ul class="social">
    <li class="social__item"><span class="social__icon"></span>/joinhourforfun</li>
    <li class="social__item"><span class="social__icon"></span>@joinhour4fun</li>
    <li class="social__item"><span class="social__icon"></span>/joinhour4fun</li>
  </ul>
</section>

</body>
</html>
```